Brisk Nibbles natural dog treats

We need a packaging design for a new brand of natural dog treats named Brisk Nibbles. Need the color scheme and template for the line of products that will be on flexible pouches or stand upright gusseted pouches.

Target Market(s)

Mass appeal with the majority being female. This will be a grocery store brand moderate price.

Industry/Entity Type

Grocery Store

Font styles to use
Serif
Sans Serif

Requirements
Must have
• Clean bright colors preferably yellow light blue etc. Very clean, memorable and simple packaging. This being a natural product it should also show natural with the packaging.
Nice to have
• Dog 30-50% of the packaging to be clear to show the product.
Should not have
• Not busy
Too much information on the front.

```html
<!DOCTYPE html>
<html lang="en">
<head>
<meta charset="utf-8">
<title>Brisk Nibbles Beef Sticks Pouch</title>
<link rel="stylesheet" href="https://fonts.googleapis.com/css2?family=Fjalla+One&family=Londrina+Solid:wght@400;900&family=Nunito:wght@800&display=swap">
<style>
  :root {
    --bg-orange: #f78a1d;
    --pouch-orange: #f59a2c;
    --band-orange: #ec8220;
    --deep-purple: #3b1c78;
    --side-purple: #44208a;
    --white: #ffffff;
    --product-light: #c8734a;
    --product-dark: #8a3d22;
  }
  * { margin: 0; padding: 0; box-sizing: border-box; }
  html, body { width: 1200px; height: 960px; overflow: hidden; }
  body { background: var(--bg-orange); position: relative; font-family: "Fjalla One", sans-serif; }

  .pouch { position: absolute; left: 240px; top: 70px; width: 720px; height: 820px; display: flex; }

  .gusset {
    width: 170px; height: 100%;
    background: linear-gradient(180deg, var(--band-orange) 0 8%, var(--side-purple) 8% 100%);
    position: relative;
  }
  .gusset-name {
    position: absolute; left: 50%; top: 56%;
    transform: translate(-50%, -50%) rotate(-90deg);
    white-space: nowrap;
    font-family: "Nunito", sans-serif; font-weight: 800;
    font-size: 64px; color: var(--white);
  }

  .front {
    width: 550px; height: 100%;
    background: var(--pouch-orange);
    position: relative; text-align: center;
    color: var(--deep-purple);
  }
  .category { position: absolute; top: 44px; width: 100%; font-size: 22px; letter-spacing: 0.5px; }
  .brand-band {
    position: absolute; top: 100px; width: 100%; height: 84px;
    background: var(--band-orange);
    display: flex; align-items: center; justify-content: center; gap: 14px;
  }
  .brand-dot { width: 34px; height: 34px; border-radius: 50%; background: var(--white); }
  .brand-name { font-family: "Nunito", sans-serif; font-weight: 800; font-size: 40px; color: var(--white); }

  .product-title { position: absolute; top: 196px; width: 100%; font-family: "Londrina Solid", sans-serif; font-weight: 900; line-height: 0.9; }
  .product-title .line-1 { display: block; font-size: 180px; letter-spacing: 4px; }
  .product-title .line-2 { display: block; font-size: 118px; letter-spacing: 2px; }

  .window {
    position: absolute; top: 486px; left: 50%; transform: translateX(-50%);
    width: 380px; height: 170px; border-radius: 60px;
    border: 10px solid var(--band-orange);
    background: repeating-linear-gradient(90deg, var(--product-light) 0 22px, var(--product-dark) 22px 30px);
  }

  .tagline { position: absolute; top: 668px; width: 100%; font-size: 38px; }
  .claims-band {
    position: absolute; top: 716px; width: 100%; height: 0;
  }
  .claims-band { top: 710px; height: 0; }

  .purple-band {
    position: absolute; top: 712px; width: 100%; height: 0;
  }
</style>
</head>
<body>
<style>
  .benefit-band {
    position: absolute; top: 712px; left: 0; width: 100%; height: 46px;
  }
  .info-band {
    position: absolute; top: 712px; width: 100%; height: 0;
  }
  .feature-band {
    position: absolute; top: 714px; width: 100%; height: 0;
  }
</style>
<style>
  .front .feature-panel {
    position: absolute; top: 716px; left: 0; width: 100%; height: 0;
  }
</style>
<style>
  .front .benefits {
    position: absolute; left: 0; top: 0; width: 100%;
  }
</style>
<style>
  .front .perks {
    position: absolute; top: 0; left: 0;
  }
</style>
<style>
  /* layout of lower front section */
  .front .lower { position: absolute; left: 0; top: 712px; width: 100%; height: 108px; }
  .front .lower-band { position: absolute; inset: 0 0 40px 0; background: var(--deep-purple); }
  .front .subline { position: absolute; top: 4px; width: 100%; font-size: 22px; color: var(--white); }
  .front .badges { position: absolute; top: 30px; left: 0; width: 100%; display: none; }
  .front .footer { position: absolute; bottom: 0; width: 100%; height: 40px; background: var(--pouch-orange); }
</style>

<div class="pouch">
  <div class="gusset">
    <span class="gusset-name">Brisk Nibbles</span>
  </div>

  <div class="front">
    <div class="category">COMPLEMENTARY PET FOOD FOR DOGS</div>

    <div class="brand-band">
      <span class="brand-dot"></span>
      <span class="brand-name">Brisk Nibbles</span>
    </div>

    <h1 class="product-title">
      <span class="line-1">BEEF</span>
      <span class="line-2">STICKS</span>
    </h1>

    <div class="window" role="img" aria-label="Clear window showing the beef sticks inside"></div>

    <div class="tagline">NATURAL DOG TREATS</div>

    <div class="lower">
      <div class="lower-band"></div>
      <div class="subline">HEALTY AND DELICIOUS</div>
    </div>
  </div>
</div>

<style>
  .front .tagline { top: 662px; }
  .front .lower { top: 708px; height: 112px; }
  .front .lower-band { position: absolute; top: 0; left: 0; right: 0; height: 112px; bottom: auto; }
  .claim-row { position: absolute; top: 38px; left: 0; width: 100%; display: flex; justify-content: center; gap: 36px; }
  .claim {
    width: 66px; height: 66px; border-radius: 50%;
    border: 2px solid var(--white); color: var(--white);
    font-size: 13px; line-height: 1.1;
    display: flex; align-items: center; justify-content: center; text-align: center;
  }
  .closing { position: absolute; top: 722px; }
</style>
<style>
  .pouch { height: 880px; top: 40px; }
  .recipe { position: absolute; top: 822px; width: 100%; font-size: 28px; color: var(--deep-purple); }
  .net-weight { position: absolute; top: 856px; width: 100%; font-size: 16px; color: var(--deep-purple); }
  .net-weight small { display: block; font-size: 10px; }
</style>

<div class="pouch" style="pointer-events:none">
  <div style="width:170px"></div>
  <div class="front" style="background:transparent">
    <div class="lower" style="background:transparent">
      <div class="claim-row">
        <div class="claim">TASTY<br>BEEF</div>
        <div class="claim">FARM<br>FRESH</div>
        <div class="claim">GLUTEN<br>FREE</div>
      </div>
    </div>
    <div class="recipe">FAMILY RECIPE DOGS LOVE</div>
  </div>
</div>
</body>
</html>
```